Purrline Fest Ticket Card Design

We’re looking to create a complimentary “ticket” card for Purrline Fest that can be handed out physically. We host an event for cat lovers. The card should feel special and collectible. Size will be a standard business card (3.5" x 2") Orientation is open to designer recommendation. This ticket will be used as a complimentary entry pass for select guests, partners, & giveaways. Key elements to Include are the Purrline Fest logo (provided), the words “Complimentary Ticket” or similar wording (open to creative phrasing and cat puns) A blank space for the Event date (to be written in) & Ticket number (to be written in) . Event Name is always "Purrline Bazaar & Rescue Gala". We want the ticket to feel clean & modern but slightly playful with a cat-inspired touch (think clever, not kitschy). Could include a subtle cat motif or texture (e.g., whisker lines, paw detail, soft patterning) Open to unique layout ideas that still leave clear writing space. Avoid overcrowding of elements. Ticket should also have fine print "This ticket is not redeemable for cash and cannot be combined with any other offers or discounts, can only be used for the date indicated"

Target Market(s)

Women

Industry/Entity Type

pets

Colors
6B429C
8869AF
B7A5CE
E3DAEB
F3F0F8

Requirements
Must have
• Purrline Fest Logo & words around complimentary ticket as well as the fine print
Nice to have
• cat-inspired touch (think clever, not kitschy). Could include a subtle cat motif or texture (e.g., whisker lines, paw detail, soft patterning)
Should not have
• should not look cartoony

```html
<!DOCTYPE html>
<html lang="en">
<head>
<meta charset="utf-8">
<title>Purrline Fest Complimentary Ticket</title>
<link href="https://fonts.googleapis.com/css2?family=Lexend:wght@400;500;600&display=swap" rel="stylesheet">
<style>
  :root {
    --purple-deep: #6B429C;
    --purple: #8869AF;
    --lilac: #B7A5CE;
    --lilac-pale: #E3DAEB;
    --mist: #F3F0F8;
    --ink: #222026;
    --panel: #29262b;
    --gold: #f2d78a;
    --gold-deep: #d99a3c;
    --cream: #f7e39a;
    --white: #ffffff;
  }
  * { margin: 0; padding: 0; box-sizing: border-box; }
  html, body { width: 1200px; height: 686px; overflow: hidden; background: var(--white); }
  .ticket {
    position: relative;
    width: 1200px;
    height: 686px;
    overflow: hidden;
    font-family: "Lexend", sans-serif;
    background: var(--white);
  }
  .curves { position: absolute; inset: 0; }
  .event-band {
    position: absolute;
    left: 62px; top: 70px;
    width: 516px; height: 126px;
    background: var(--purple);
    transform: rotate(-2deg);
    box-shadow: 0 10px 18px rgba(80, 50, 120, 0.18);
  }
  .event-band span {
    position: absolute;
    left: 36px; top: 24px;
    font-size: 64px; font-weight: 500;
    color: var(--white);
    letter-spacing: -1px;
    line-height: 1;
  }
  .event-title {
    position: absolute;
    left: 116px; top: 196px;
    font-size: 82px; font-weight: 500;
    line-height: 100px;
    letter-spacing: -2px;
    color: var(--ink);
  }
  .paw-mark, .heart-mark { position: absolute; border-radius: 50%; }
  .paw-mark { background: var(--purple-deep); width: 72px; height: 72px; }
  .heart-mark { background: var(--gold); width: 30px; height: 28px; }
  .write-box {
    position: absolute;
    border: 2px dashed #3a3a3a;
  }
  .write-box--details { left: 62px; top: 431px; width: 418px; height: 180px; }
  .write-box--stub { left: 501px; top: 431px; width: 182px; height: 180px; }
  .field-icon { position: absolute; left: 118px; width: 40px; height: 40px; }
  .field-icon--date { top: 466px; }
  .field-icon--number { top: 534px; }
  .pass-panel {
    position: absolute;
    left: 831px; top: 0;
    width: 369px; height: 686px;
    background: var(--panel);
    color: var(--white);
    text-align: center;
  }
  .pass-panel__texture {
    position: absolute; inset: 0;
    background: radial-gradient(circle at 50% 40%, #333036 0%, var(--panel) 70%);
  }
  .brand-name {
    position: absolute;
    left: 0; right: 0; top: 128px;
    font-size: 54px; font-weight: 600;
    line-height: 1.05;
    color: var(--white);
  }
  .pass-label {
    position: absolute;
    left: 0; right: 0; top: 305px;
    font-size: 31px; font-weight: 400;
    line-height: 40px;
  }
  .fine-print {
    position: absolute;
    left: 50px; right: 50px; top: 416px;
    font-size: 15.5px; font-weight: 400;
    line-height: 21px;
  }
  .admits {
    position: absolute;
    left: 0; right: 0; top: 556px;
    font-size: 29px; font-weight: 400;
    color: var(--cream);
  }
</style>
</head>
<body>
<div class="ticket">
  <svg class="curves" width="1200" height="686" viewBox="0 0 1200 686" aria-hidden="true">
    <path d="M-10 58 C 120 10, 300 20, 420 110 S 470 40, 500 -10" fill="none" stroke="var(--lilac)" stroke-width="3"/>
    <path d="M660 686 C 640 600, 690 560, 760 540 S 830 480, 835 470" fill="none" stroke="var(--lilac)" stroke-width="3"/>
  </svg>

  <div class="event-band"><span>Purrline</span></div>
  <h1 class="event-title">Bazaar &amp;<br>Rescue Gala.</h1>

  <div class="paw-mark" style="left:580px;top:80px" role="img" aria-label="Purple paw print"></div>
  <div class="paw-mark" style="left:668px;top:146px" role="img" aria-label="Purple paw print"></div>
  <div class="heart-mark" style="left:86px;top:66px" role="img" aria-label="Gold heart"></div>
  <div class="heart-mark" style="left:754px;top:294px;background:var(--gold-deep)" role="img" aria-label="Bronze heart"></div>
  <div class="heart-mark" style="left:346px;top:388px;width:24px;height:22px" role="img" aria-label="Gold heart"></div>
  <div class="heart-mark" style="left:74px;top:414px;width:38px;height:34px" role="img" aria-label="Gold heart"></div>

  <div class="write-box write-box--details"></div>
  <div class="write-box write-box--stub"></div>

  <svg class="field-icon field-icon--date" viewBox="0 0 40 40" role="img" aria-label="Event date">
    <rect x="3" y="6" width="34" height="31" rx="5" fill="var(--purple-deep)"/>
    <rect x="10" y="2" width="4" height="8" rx="2" fill="var(--purple-deep)"/>
    <rect x="26" y="2" width="4" height="8" rx="2" fill="var(--purple-deep)"/>
    <rect x="3" y="12" width="34" height="2" fill="var(--white)"/>
    <g fill="var(--white)">
      <rect x="9" y="18" width="5" height="4" rx="1"/><rect x="17.5" y="18" width="5" height="4" rx="1"/><rect x="26" y="18" width="5" height="4" rx="1"/>
      <rect x="9" y="26" width="5" height="4" rx="1"/><rect x="17.5" y="26" width="5" height="4" rx="1"/><rect x="26" y="26" width="5" height="4" rx="1"/>
    </g>
  </svg>
  <svg class="field-icon field-icon--number" viewBox="0 0 40 40" role="img" aria-label="Ticket number">
    <path d="M4 14 L33 6 L35 12 L6 20 Z" fill="var(--purple-deep)"/>
    <path d="M3 16 H37 V22 A4 4 0 0 0 37 30 V36 H3 V30 A4 4 0 0 0 3 22 Z" fill="var(--purple-deep)"/>
    <rect x="11" y="23" width="12" height="2" fill="var(--white)"/>
    <rect x="11" y="28" width="9" height="2" fill="var(--white)"/>
  </svg>

  <aside class="pass-panel">
    <div class="pass-panel__texture" role="img" aria-label="Soft paw print pattern on a dark background"></div>
    <div class="brand-name">Purrline<br>Fest</div>
    <p class="pass-label">Complimentary<br>Ticket</p>
    <p class="fine-print">This ticket is not redeemable for cash and cannot be combined with other offers or discounts. Valid only for the date indicated.</p>
    <p class="admits">Admits 1 Person</p>
  </aside>
</div>
</body>
</html>
```